Haverill’s

I would like a high class looking card with my logo and contact details (as per uploaded) Elegant, professional and highest quality feel

The following text included …..
“All commercial and residential painting work, large or small. Highest quality finishes and service.”

Industry/Entity Type

Painting

Contact Information for Business Card

Name, phone number, address, email address, company logo

Requirements
Must have
• Double sided

```html
<!DOCTYPE html>
<html lang="en">
<head>
<meta charset="utf-8">
<title>Haverill’s Business Card</title>
<link rel="stylesheet" href="https://fonts.googleapis.com/css2?family=Cinzel:wght@400;500&family=Questrial&family=Montserrat:wght@600&display=swap">
<style>
  :root {
    --bg: #3a3a3a;
    --paper: #f2f2f2;
    --ink: #2e2e2e;
    --gold: #b5874a;
    --card-dark: #2a2a2a;
    --card-dark-edge: #1f1f1f;
    --silver: #d9d9d9;
    --silver-dim: #a8a8a8;
  }
  * { margin: 0; padding: 0; box-sizing: border-box; }
  html, body { width: 1200px; height: 1200px; overflow: hidden; }
  body {
    background: var(--bg);
    position: relative;
    font-family: "Questrial", sans-serif;
  }
  .card {
    position: absolute;
    left: 150px;
    width: 900px;
    height: 514px;
    border-radius: 40px;
    overflow: hidden;
    box-shadow: 0 14px 36px rgba(0,0,0,0.45);
  }
  .card-back { top: 66px; background: var(--paper); }
  .card-front {
    top: 620px;
    background: radial-gradient(ellipse at 60% 35%, #353535 0%, var(--card-dark) 55%, var(--card-dark-edge) 100%);
  }

  /* back side: contact */
  .brand-mark {
    position: absolute;
    top: 120px;
    right: 90px;
    display: flex;
    align-items: center;
    gap: 18px;
  }
  .brand-mark .dot {
    width: 26px; height: 26px; border-radius: 50%;
    background: var(--gold);
  }
  .brand-mark .brand-name {
    font-family: "Cinzel", serif;
    font-weight: 500;
    font-size: 46px;
    color: var(--gold);
    letter-spacing: 2px;
  }
  .contact {
    position: absolute;
    left: 70px;
    top: 236px;
    color: var(--ink);
  }
  .contact .full-name {
    font-family: "Montserrat", sans-serif;
    font-weight: 600;
    font-size: 34px;
    color: var(--gold);
    letter-spacing: -1px;
    line-height: 1;
  }
  .contact .position {
    font-size: 24px;
    line-height: 1.1;
    margin-bottom: 14px;
  }
  .contact-list { list-style: none; }
  .contact-list li {
    display: flex;
    align-items: flex-start;
    gap: 12px;
    font-size: 22px;
    line-height: 1.25;
    margin-bottom: 3px;
  }
  .contact-list svg { width: 22px; height: 22px; flex: none; margin-top: 3px; fill: var(--gold); }
  .tagline {
    position: absolute;
    left: 300px;
    right: 60px;
    bottom: 58px;
    font-family: "Cinzel", serif;
    font-size: 19px;
    color: var(--ink);
    text-align: center;
    line-height: 1.35;
    letter-spacing: 0.5px;
  }

  /* front side: brand */
  .front-brand {
    position: absolute;
    top: 50%;
    left: 50%;
    transform: translate(-50%, -50%);
    display: flex;
    align-items: center;
    gap: 26px;
  }
  .front-brand .brand-name {
    font-family: "Cinzel", serif;
    font-weight: 400;
    font-size: 84px;
    color: var(--silver);
    letter-spacing: 3px;
  }
  .front-brand .ring {
    width: 34px; height: 34px; border-radius: 50%;
    background: var(--silver-dim);
  }
</style>
</head>
<body>
  <section class="card card-back" aria-label="Card back, contact side">
    <div class="brand-mark">
      <span class="dot"></span>
      <span class="brand-name">Haverill’s</span>
    </div>

    <div class="contact">
      <p class="full-name">FULL NAME</p>
      <p class="position">POSITION</p>
      <ul class="contact-list">
        <li>
          <svg viewBox="0 0 24 24" aria-hidden="true"><path d="M6.6 10.8c1.4 2.8 3.8 5.1 6.6 6.6l2.2-2.2c.3-.3.7-.4 1-.2 1.1.4 2.3.6 3.6.6.6 0 1 .4 1 1V20c0 .6-.4 1-1 1C10.6 21 3 13.4 3 4c0-.6.4-1 1-1h3.5c.6 0 1 .4 1 1 0 1.3.2 2.5.6 3.6.1.3 0 .7-.2 1z"/></svg>
          <span>(000) 000 0000</span>
        </li>
        <li>
          <svg viewBox="0 0 24 24" aria-hidden="true"><path d="M2 5h20v14H2z M4 7v.4l8 5.2 8-5.2V7z" fill-rule="evenodd"/></svg>
          <span>email@company.com</span>
        </li>
        <li>
          <svg viewBox="0 0 24 24" aria-hidden="true"><path d="M12 2a10 10 0 1 0 0 20 10 10 0 0 0 0-20zm0 2c.9 1 1.7 2.6 2 4.5h-4C10.3 6.6 11.1 5 12 4zM9.8 10.5h4.4a14 14 0 0 1 0 3H9.8a14 14 0 0 1 0-3zM4.3 10.5h3.5a16 16 0 0 0 0 3H4.3a8 8 0 0 1 0-3zm11.9 0h3.5a8 8 0 0 1 0 3h-3.5a16 16 0 0 0 0-3zM10 15.5h4c-.3 1.9-1.1 3.5-2 4.5-.9-1-1.7-2.6-2-4.5z"/></svg>
          <span>www.company.com</span>
        </li>
        <li>
          <svg viewBox="0 0 24 24" aria-hidden="true"><path d="M12 2a7 7 0 0 0-7 7c0 5 7 13 7 13s7-8 7-13a7 7 0 0 0-7-7zm0 9.5a2.5 2.5 0 1 1 0-5 2.5 2.5 0 0 1 0 5z"/></svg>
          <span>123 Name Street,000<br>Your City,00000-000</span>
        </li>
      </ul>
    </div>

    <p class="tagline">All commercial and residential painting work,<br>large or small. Highest quality finishes and service.</p>
  </section>

  <section class="card card-front" aria-label="Card front, brand side">
    <div class="front-brand">
      <span class="brand-name">Haverill’s</span>
      <span class="ring"></span>
    </div>
  </section>
</body>
</html>
```